Paws and Meadows is a dog walking service that offers home boarding and pet taxi

I am looking for a eye catching A5 leaflet/flyer design for my dog walking business Paws and Meadows.

The flyer must have my company logo on it (jpeg), a picture of my van (jpeg) and a picture of dogs playing (jpegs 1-5).

The fonts must be easy to read. I am not set on any colour scheme but do like the idea of having a natural background. IE. Green grass and blue sky or some forest setting with green trees. If you don't like this idea or its hard to work with don't worry I am open minded so be creative and do what you thinks best.

I'll provide quick feedback to designs that i like and so we can work together.

The flyers must contain the following:

60 minute group and individual walks
GPS Tracked Walks
Home Boarding
Pet Taxi
Puppy/Pet visits

Offer: 50% off first weeks dogs walks with this flyer.

As well as containing my contact info:

07519306284
www.pawsmeadowsgroup.co.uk
pawsmeadowsgroup@brightmailbox.co.uk

Chatterbook, Quipster and Snapfolio logos must be present as well.

Thanks and Good luck!

Target Market(s)

ANYONE WHO NEEDS THEIR DOG WALKED OR LOOKED AFTER WHEN THEY ARE ON HOLIDAY

Industry/Entity Type

Business

Contact Information for Business Card

THE BUSINESS CARD MUST DISPLAY THE LOGO THAT HAS BEEN UPLOADED IN A FILE. IT MUST LOOK SHARP AND PROFESSIONAL. CONTAIN ALL CONTACT INFO AND HAVE SERVICES OFFERED. SEE PROJECT DESCRIPTION FOR FLYER.

Font styles to use
Serif
Sans Serif

Requirements
Must have
• SEE PROJECT DESCRIPTION
Nice to have
• IT WOULD BE NICE TO HAVE PHOTOS OF MY VAN AND DOGS PLAYING. I HAVE UPLOADED SOME PICS OF VAN TO BE USED AND THERE ARE PICS OF DOGS PLAYING THAT COULD BE USED.

```html
<!DOCTYPE html>
<html lang="en">
<head>
<meta charset="utf-8">
<title>Paws and Meadows – A5 Flyer</title>
<link href="https://fonts.googleapis.com/css2?family=Sniglet:wght@400;800&display=swap" rel="stylesheet">
<style>
  :root{
    --page:#ece7df;
    --sky-top:#5db8ea;
    --sky-mid:#b9e3f8;
    --sky-light:#e9f7fd;
    --grass-light:#c4dc3a;
    --grass-mid:#6fae2a;
    --grass-dark:#2f7a1c;
    --ink:#2b2b2b;
    --white:#ffffff;
    --orange:#f39a1e;
    --orange-light:#fbc25a;
    --photo-warm:#8a6a4a;
    --photo-green:#5c8a3a;
    --van-light:#eef1f4;
    --van-mid:#b9c1c9;
    --chatter:#4a6fd6;
    --quip:#3aa8e6;
    --snap:#e25c9c;
  }
  *{box-sizing:border-box;margin:0;padding:0}
  html,body{width:993px;height:1200px;overflow:hidden}
  body{background:var(--page);font-family:"Sniglet",system-ui,sans-serif;color:var(--ink);position:relative}

  .flyer{position:absolute;left:86px;top:20px;width:820px;height:1160px;overflow:hidden;
    box-shadow:0 6px 22px rgba(0,0,0,.18)}
  .flyer__scene{position:absolute;inset:0;
    background:linear-gradient(180deg,var(--sky-top) 0%,var(--sky-mid) 22%,var(--sky-light) 50%,var(--grass-light) 60%,var(--grass-mid) 74%,var(--grass-dark) 100%)}

  .brand{position:absolute;left:40px;top:70px;width:360px;display:flex;flex-direction:column;align-items:center}
  .brand__mark{width:120px;height:120px;border-radius:50%;border:5px solid var(--orange);background:rgba(255,255,255,.35)}
  .brand__name{margin-top:14px;font-weight:800;font-size:28px;color:var(--ink);text-transform:uppercase;white-space:nowrap;text-align:center}
  .brand__tag{margin-top:2px;font-size:12px;letter-spacing:4px;color:var(--ink);text-transform:uppercase}

  .headline{position:absolute;left:420px;top:48px;width:360px;text-align:center;font-weight:800;font-size:34px;line-height:1.1;text-transform:uppercase;color:var(--ink)}

  .photo{position:absolute;border-radius:50%;border:6px solid var(--orange);box-shadow:0 3px 8px rgba(0,0,0,.25)}
  .photo--top{left:560px;top:160px;width:170px;height:170px;background:radial-gradient(circle at 40% 40%,#4a3a30,var(--photo-warm) 70%,#9a9a8a)}
  .photo--mid{left:620px;top:300px;width:160px;height:160px;background:radial-gradient(circle at 50% 45%,#c89a5a,#3a3a2a 60%,var(--photo-green))}
  .photo--low{left:60px;top:640px;width:170px;height:170px;background:radial-gradient(circle at 50% 50%,#c9a27a,var(--photo-green) 75%)}

  .services{position:absolute;left:60px;top:320px;width:530px;list-style:none}
  .services__item{display:flex;align-items:center;gap:12px;font-size:24px;font-weight:800;margin-bottom:16px;color:var(--ink);white-space:nowrap}
  .services__paw{width:24px;height:24px;flex:none}

  .van{position:absolute;left:410px;top:470px;width:410px;height:250px;border-radius:18px 0 0 18px;
    background:linear-gradient(160deg,var(--van-light) 0%,var(--white) 40%,var(--van-mid) 100%)}

  .offer{position:absolute;left:300px;top:640px;width:180px;height:180px;border-radius:50%;
    background:radial-gradient(circle at 40% 35%,var(--orange-light),var(--orange));
    display:flex;flex-direction:column;align-items:center;justify-content:center;text-align:center;color:var(--ink);box-shadow:0 3px 8px rgba(0,0,0,.2)}
  .offer__big{font-size:42px;font-weight:800;line-height:1}
  .offer__big small{font-size:16px}
  .offer__text{font-size:15px;font-weight:800;line-height:1.2;margin-top:4px}

  .social{position:absolute;right:40px;top:770px;text-align:right;color:var(--white)}
  .social__label{font-size:20px;font-weight:800;margin-bottom:10px}
  .social__list{display:flex;flex-direction:column;gap:8px;align-items:flex-end;list-style:none}
  .social__item{display:flex;align-items:center;gap:8px;font-size:18px;font-weight:800}
  .social__dot{width:22px;height:22px;border-radius:50%}
  .social__dot--chatter{background:var(--chatter)}
  .social__dot--quip{background:var(--quip)}
  .social__dot--snap{background:var(--snap)}

  .contact{position:absolute;left:50px;bottom:50px;color:var(--white);text-shadow:0 2px 4px rgba(0,0,0,.3)}
  .contact__phone{font-size:66px;font-weight:800;line-height:1.05;letter-spacing:1px}
  .contact__web{font-size:30px;font-weight:400;margin-top:6px}
  .contact__email{font-size:26px;font-weight:400;margin-top:2px}
</style>
</head>
<body>
  <main class="flyer">
    <div class="flyer__scene" role="img" aria-label="Blue sky over a green field with dogs running and playing"></div>

    <header class="brand">
      <div class="brand__mark"></div>
      <div class="brand__name">Paws and Meadows</div>
      <div class="brand__tag">Dog Walking Service</div>
    </header>

    <h1 class="headline">Caring for your<br>furry friend</h1>

    <div class="photo photo--top" role="img" aria-label="Photo of a dark brown dog"></div>
    <div class="photo photo--mid" role="img" aria-label="Photo of two dogs playing with a stick"></div>

    <ul class="services">
      <li class="services__item"><svg class="services__paw" viewBox="0 0 28 28"><g fill="#2b2b2b"><ellipse cx="14" cy="19" rx="7" ry="6"/><circle cx="5" cy="11" r="3"/><circle cx="10.5" cy="5.5" r="3"/><circle cx="17.5" cy="5.5" r="3"/><circle cx="23" cy="11" r="3"/></g></svg>60 minute group &amp; individual walks</li>
      <li class="services__item"><svg class="services__paw" viewBox="0 0 28 28"><g fill="#2b2b2b"><ellipse cx="14" cy="19" rx="7" ry="6"/><circle cx="5" cy="11" r="3"/><circle cx="10.5" cy="5.5" r="3"/><circle cx="17.5" cy="5.5" r="3"/><circle cx="23" cy="11" r="3"/></g></svg>GPS Tracked Walks</li>
      <li class="services__item"><svg class="services__paw" viewBox="0 0 28 28"><g fill="#2b2b2b"><ellipse cx="14" cy="19" rx="7" ry="6"/><circle cx="5" cy="11" r="3"/><circle cx="10.5" cy="5.5" r="3"/><circle cx="17.5" cy="5.5" r="3"/><circle cx="23" cy="11" r="3"/></g></svg>Home Boarding</li>
      <li class="services__item"><svg class="services__paw" viewBox="0 0 28 28"><g fill="#2b2b2b"><ellipse cx="14" cy="19" rx="7" ry="6"/><circle cx="5" cy="11" r="3"/><circle cx="10.5" cy="5.5" r="3"/><circle cx="17.5" cy="5.5" r="3"/><circle cx="23" cy="11" r="3"/></g></svg>Pet Taxi</li>
      <li class="services__item"><svg class="services__paw" viewBox="0 0 28 28"><g fill="#2b2b2b"><ellipse cx="14" cy="19" rx="7" ry="6"/><circle cx="5" cy="11" r="3"/><circle cx="10.5" cy="5.5" r="3"/><circle cx="17.5" cy="5.5" r="3"/><circle cx="23" cy="11" r="3"/></g></svg>Puppy/Pet visits</li>
    </ul>

    <div class="van" role="img" aria-label="Photo of the company's white branded van"></div>

    <div class="photo photo--low" role="img" aria-label="Photo of two dogs playing on grass"></div>

    <div class="offer">
      <div class="offer__big">50%<small> off</small></div>
      <div class="offer__text">first weeks<br>dogs walks with<br>this flyer.</div>
    </div>

    <aside class="social">
      <div class="social__label">Follow us on</div>
      <ul class="social__list">
        <li class="social__item"><span class="social__dot social__dot--chatter"></span>Chatterbook</li>
        <li class="social__item"><span class="social__dot social__dot--quip"></span>Quipster</li>
        <li class="social__item"><span class="social__dot social__dot--snap"></span>Snapfolio</li>
      </ul>
    </aside>

    <footer class="contact">
      <div class="contact__phone">07519306284</div>
      <div class="contact__web">www.pawsmeadowsgroup.co.uk</div>
      <div class="contact__email">pawsmeadowsgroup@brightmailbox.co.uk</div>
    </footer>
  </main>
</body>
</html>
```